Home Page Website Design

The Site width is 1000 px. I've attached a Balsamiq mockup as a design layout guide. The design needs to be flat and clean. Please stick to the pixel dimensions of the mock up as the site will be responsive. I've also attached the logos used on the mockup for positional purposes.

Colours to use: Black, Grey, Green (Logo tie in) & green complementary colours.

Green (Logo tie in)
White Background
Titles: Black (Roboto Bold 700)
Text: Dark Grey (Roboto Normal 400)

Look & Style Example
http://www.brindlowlearn.org.uk/

Type Face
Google Fonts - Roboto

These are just guidelines, please feel free to use you own creative judgment.

Thanks

```html
<!DOCTYPE html>
<html lang="en">
<head>
<meta charset="utf-8">
<title>Brellavane Teaching Collective – Home</title>
<link rel="stylesheet" href="https://fonts.googleapis.com/css2?family=Noto+Serif:wght@400;700&display=swap">
<style>
  :root {
    --topbar: #666666;
    --topbar-text: #ffffff;
    --page: #ffffff;
    --band: #f3f3f3;
    --rule: #d6d6d6;
    --panel-border: #c8c8c8;
    --field: #555555;
    --field-text: #bdbdbd;
    --accent-blue: #1a9ad6;
    --button-border: #0d5f86;
    --brand-green: #1cb35a;
    --ink: #111111;
    --body-grey: #9a9a9a;
    --photo-light: #efe6d8;
    --photo-mid: #c9a98a;
    --photo-dark: #5a4a55;
  }
  * { box-sizing: border-box; margin: 0; padding: 0; }
  html, body {
    width: 1200px; height: 626px; overflow: hidden;
    background: var(--page);
    font-family: "Noto Serif", Georgia, serif;
  }
  .page { position: relative; width: 1200px; height: 626px; }

  .top-bar {
    position: absolute; left: 0; top: 0; width: 1200px; height: 47px;
    background: var(--topbar); color: var(--topbar-text);
  }
  .top-bar__contact { position: absolute; left: 29px; top: 12px; font-size: 16px; }
  .top-bar__login {
    position: absolute; right: 20px; top: 11px; font-size: 17px; font-weight: 700;
    display: flex; align-items: center; gap: 6px;
  }

  .header { position: absolute; left: 0; top: 47px; width: 1200px; height: 167px; }
  .brand {
    position: absolute; left: 42px; top: 56px;
    display: flex; align-items: center; gap: 10px;
    color: var(--brand-green); font-size: 17px; font-weight: 700; line-height: 1.25;
  }
  .brand__dot { width: 34px; height: 34px; border-radius: 50%; background: var(--brand-green); flex: none; }

  .register {
    position: absolute; left: 853px; top: 28px; width: 323px; height: 64px;
    background: #f2f2f2; border: 1px solid var(--panel-border);
  }
  .register__title { position: absolute; left: 7px; top: 5px; font-size: 16px; color: #333; }
  .field {
    background: var(--field); color: var(--field-text); font-family: inherit;
    font-size: 14px; padding: 0 8px; display: flex; align-items: center;
  }
  .register__field { position: absolute; left: 6px; top: 28px; width: 218px; height: 28px; }
  .btn {
    background: var(--accent-blue); color: #fff; font-weight: 700; font-family: inherit;
    border: 1px solid var(--button-border); display: flex; align-items: center; justify-content: center;
  }
  .register__submit { position: absolute; left: 232px; top: 26px; width: 83px; height: 30px; font-size: 15px; }

  .nav-band {
    position: absolute; left: 0; top: 214px; width: 1200px; height: 81px;
    background: var(--band); border-top: 1px solid var(--rule); border-bottom: 1px solid var(--rule);
  }
  .main-nav {
    position: absolute; left: 29px; top: 31px; display: flex; gap: 20px;
    font-size: 12px; font-weight: 700; text-transform: uppercase; color: var(--ink); letter-spacing: 0.3px;
  }
  .site-search__field { position: absolute; left: 865px; top: 25px; width: 223px; height: 31px; font-size: 14px; }
  .site-search__button { position: absolute; left: 1095px; top: 25px; width: 81px; height: 31px; font-size: 15px; }

  .feature {
    position: absolute; left: 6px; top: 302px; width: 402px; height: 317px;
    border: 1px solid var(--panel-border); background: #fff;
  }
  .feature__title { text-align: center; margin-top: 25px; font-size: 24px; font-weight: 700; color: var(--ink); }
  .feature__text {
    margin: 16px 6px 0 6px; font-size: 14.4px; line-height: 19.5px; color: var(--body-grey);
  }
  .feature__more { position: absolute; left: 6px; top: 280px; width: 136px; height: 30px; font-size: 15px; }

  .slider {
    position: absolute; left: 416px; top: 302px; width: 784px; height: 322px;
    border: 1px solid var(--rule); background: #fff;
  }
  .slider__image {
    position: absolute; left: 4px; top: 5px; width: 774px; height: 309px;
    background: linear-gradient(100deg, var(--photo-light) 0%, var(--photo-mid) 45%, var(--photo-dark) 70%, var(--photo-mid) 100%);
  }
  .slider__dots { position: absolute; left: 375px; top: 274px; display: flex; gap: 13px; }
  .slider__dot {
    width: 21px; height: 21px; border-radius: 50%; font-size: 13px;
    display: flex; align-items: center; justify-content: center;
    background: rgba(255,255,255,0.45); color: #fff;
  }
  .slider__dot--active { background: #fff; color: #000; }
</style>
</head>
<body>
<div class="page">
  <div class="top-bar">
    <div class="top-bar__contact">Tel:xxxxxxxxxx | Mail: info@domain.com</div>
    <div class="top-bar__login">
      <svg width="20" height="14" viewBox="0 0 20 14" aria-hidden="true">
        <rect x="0.5" y="0.5" width="19" height="13" rx="2" fill="#e6e6e6" stroke="#999"/>
        <circle cx="6" cy="7" r="2.5" fill="#3a6fb5"/>
        <rect x="8" y="6" width="8" height="2" fill="#3a6fb5"/>
      </svg>
      Log IN
    </div>
  </div>

  <header class="header">
    <div class="brand">
      <span class="brand__dot"></span>
      <span>Brellavane Teaching<br>Collective</span>
    </div>
    <form class="register">
      <div class="register__title">Register Now</div>
      <div class="field register__field">email address...</div>
      <div class="btn register__submit">Submit</div>
    </form>
  </header>

  <div class="nav-band">
    <nav class="main-nav">
      <span>Home</span><span>About Us</span><span>Training &amp; Development</span><span>Benefits</span>
      <span>Members</span><span>What's On</span><span>Contact Us</span><span>News</span><span>Forum</span>
    </nav>
    <div class="field site-search__field">Search Our Website...</div>
    <div class="btn site-search__button">SEARCH</div>
  </div>

  <section class="feature">
    <h2 class="feature__title">New Teachers in Workshop</h2>
    <p class="feature__text">Our first workshop for newly qualified teachers brings together staff from across the member schools. Over two mornings you will plan lessons, share classroom ideas, observe experienced colleagues and build a support network that lasts well beyond your first year. Sessions are led by specialist leaders of education and cover behaviour, assessment, planning and wellbeing. Places are limited, so please register early to secure a place for your school team.</p>
    <div class="btn feature__more">Find Out More</div>
  </section>

  <section class="slider">
    <div class="slider__image" role="img" aria-label="Photo of a teacher helping young pupils write at a classroom desk"></div>
    <div class="slider__dots">
      <span class="slider__dot">1</span>
      <span class="slider__dot slider__dot--active">2</span>
    </div>
  </section>
</div>
</body>
</html>
```